Job Coaching - Mova; engaging people to improve their work experience

design a website focussed on people
with 4 tabs/pages (+2)
1) landing page
2) Professional
3) Job Coaching
4) Bio
5) Contact
6) references

I've added the text to be used in the documents. The website will be in Dutch, but I've added the translations in green just for you to understand what it is about.

I've added my logo as well, and a flyer I used already. this gives you an idea on how it could look like
Pictures you can find there as well. Other pictures can be added of course
The techical creation of the website is not needed. I need all the designs and information to be able to create it myself.

```html
<!DOCTYPE html>
<html lang="nl">
<head>
<meta charset="utf-8">
<title>Mova – Job Coaching</title>
<link href="https://fonts.googleapis.com/css2?family=Prata&family=Roboto:wght@400;500;700&family=Roboto+Condensed:wght@400;700&family=Fira+Mono:wght@500&display=swap" rel="stylesheet">
<style>
:root{
  --teal:#3aa99c;
  --teal-dark:#2f9488;
  --sky:#e1f6fb;
  --ink:#333333;
  --muted:#6d6d6d;
  --line:#e6eeee;
  --ocean-a:#0f7fae;
  --ocean-b:#27b3d6;
  --footer:#333333;
  --white:#ffffff;
}
*{box-sizing:border-box;margin:0;padding:0}
html,body{width:1200px;height:4478px;overflow:hidden}
body{font-family:"Roboto",Arial,sans-serif;color:var(--ink);background:var(--white)}
.page{position:relative;width:1200px;height:4478px;overflow:hidden}
.abs{position:absolute}
.serif{font-family:"Prata",Georgia,serif;font-weight:400}

/* header */
.hero{left:0;top:0;width:1200px;height:760px;background:linear-gradient(180deg,#d9f4fa 0%,var(--sky) 100%)}
.brand{left:150px;top:24px;display:flex;align-items:center;gap:12px}
.brand-dot{width:42px;height:42px;border-radius:50%;background:var(--teal)}
.brand-name{font-family:"Roboto",sans-serif;font-weight:700;font-size:40px;color:var(--teal);letter-spacing:2px}
.nav{left:403px;top:46px;display:flex;gap:24px;font-size:12px;font-weight:500;letter-spacing:.3px}
.nav a{color:var(--ink);text-decoration:none}
.nav a.active{color:var(--teal)}
.call{left:800px;top:25px;display:flex;align-items:center;gap:14px}
.circle{width:46px;height:46px;border-radius:50%;background:var(--teal);display:flex;align-items:center;justify-content:center}
.call small{display:block;font-size:10px;color:var(--muted)}
.call strong{font-family:"Roboto Condensed",sans-serif;font-size:17px}
.talk-btn{left:982px;top:26px;width:142px;height:44px;border-radius:22px;background:var(--teal);color:#fff;font-size:12px;font-weight:500;display:flex;align-items:center;justify-content:center;gap:8px}

.hero-title{left:146px;top:274px;font-size:36px;color:var(--teal);letter-spacing:.5px}
.hero-sub{left:146px;top:334px;font-size:17px;font-family:"Prata",serif;color:var(--ink);letter-spacing:.3px}
.hero-sub span{margin:0 16px;color:#999}
.hero-text{left:146px;top:378px;width:420px;font-size:14px;line-height:24px;color:#555}
.btn{height:46px;border-radius:23px;font-size:11px;font-weight:700;display:flex;align-items:center;justify-content:center;letter-spacing:.3px}
.btn-fill{left:143px;top:459px;width:169px;background:var(--teal);color:#fff}
.btn-line{left:329px;top:459px;width:130px;border:2px solid var(--ink);color:var(--ink)}
.portrait{left:700px;top:105px;width:360px;height:500px;border-radius:170px 170px 0 0;background:linear-gradient(180deg,#c98c6b 0%,#9b2a3a 45%,#7a1f2c 100%)}
.years{left:896px;top:386px;width:158px;height:92px;background:#fff;box-shadow:6px 6px 0 var(--teal);padding:20px 0 0 26px}
.years b{display:block;font-family:"Roboto Condensed",sans-serif;font-size:24px;color:var(--ink)}
.years small{font-size:11px;color:var(--teal)}
.scroll-line{left:218px;top:560px;height:140px;border-left:2px dashed var(--teal)}
.scroll-knob{left:188px;top:694px;width:60px;height:60px;border-radius:50%;background:#fff;box-shadow:0 2px 8px rgba(0,0,0,.12);display:flex;align-items:center;justify-content:center}
.scroll-label{left:186px;top:760px;font-size:11px;color:var(--teal);letter-spacing:2px;transform:rotate(12deg)}

/* help grid */
.sec-title{left:0;width:1200px;text-align:center;font-size:28px;color:var(--ink)}
.sec-sub{left:0;width:1200px;text-align:center;font-size:13px;line-height:25px;color:var(--muted)}
.grid{left:176px;top:904px;width:916px;height:439px;display:grid;grid-template-columns:repeat(3,1fr);grid-template-rows:repeat(2,1fr);border:1px solid var(--line)}
.cell{border:1px solid var(--line);display:flex;flex-direction:column;align-items:center;justify-content:flex-end;padding-bottom:42px;text-align:center;font-size:13px;line-height:22px;color:var(--ink)}
.cell svg{margin-bottom:22px}
.cell.on{background:var(--teal);color:#fff}
.cta{left:468px;top:1379px;width:264px;height:43px;background:var(--teal);color:#fff;font-size:11px;font-weight:700;display:flex;align-items:center;justify-content:center;gap:14px;letter-spacing:.3px}

/* services */
.services{left:0;top:1480px;width:1200px;height:537px;background:var(--teal)}
.services .sec-title,.services .sec-sub{color:#fff}
.card{top:174px;width:205px;height:275px;background:#fff}
.card .ph{height:210px;background:linear-gradient(180deg,#d8dee4,#8b97a3)}
.card .badge{position:absolute;left:72px;top:178px;width:62px;height:62px;border-radius:50%;background:#fff;display:flex;align-items:center;justify-content:center}
.card p{position:absolute;left:0;bottom:18px;width:100%;text-align:center;font-size:13px;font-weight:500}
.next{left:1049px;top:320px;width:26px;height:26px;border-radius:50%;background:#fff;display:flex;align-items:center;justify-content:center}

/* explore */
.explore{left:0;top:2017px;width:1200px;height:748px;background:radial-gradient(ellipse at 55% 40%,var(--ocean-b) 0%,var(--ocean-a) 70%,#0b5f85 100%)}
.explore .sec-title,.explore .sec-sub{color:#fff}
.explore .sec-sub{font-weight:500}
.step{color:#fff;font-weight:700;font-size:16px}

/* coach */
.coach-title{left:152px;top:2915px;font-size:28px}
.point{left:142px;display:flex;gap:20px;width:420px}
.point b{font-family:"Fira Mono",monospace;font-style:italic;font-size:30px;color:var(--ink);min-width:40px}
.point p{font-size:13px;line-height:22px;color:#555;padding-top:2px}
.sign{left:150px;top:3250px;width:130px;height:44px;background:linear-gradient(90deg,#d6efec,#bfe5e0)}
.coach-ring{left:660px;top:2846px;width:405px;height:540px;border:1px solid var(--teal);border-radius:210px}
.coach-photo{left:643px;top:2840px;width:405px;height:540px;border-radius:210px;background:linear-gradient(180deg,#c9d3cf 0%,#b8866c 35%,#7a1f2c 70%,#4e1420 100%)}

/* sign up */
.signup{left:0;top:3443px;width:1200px;height:700px;background:var(--teal)}
.signup .sec-title,.signup .sec-sub{color:#fff}
.field{border:1px solid rgba(255,255,255,.7);border-radius:3px}
.field label{position:absolute;left:16px;top:-8px;background:var(--teal);padding:0 6px;font-size:11px;color:#fff}
.field span{position:absolute;left:22px;top:18px;font-size:12px;color:rgba(255,255,255,.55)}
.submit{left:513px;top:3974px;width:177px;height:40px;background:#666;color:#fff;font-size:12px;font-weight:700;display:flex;align-items:center;justify-content:center}

/* footer */
.footer{left:0;top:4100px;width:1200px;height:378px;background:var(--footer)}
.foot-brand{left:165px;top:4240px;display:flex;align-items:center;gap:12px}
.foot-brand .brand-name{font-size:40px}
.cert{left:173px;top:4332px;width:125px;height:36px;background:#fff;border-bottom:4px solid #1e4b8f}
.cert-2{left:327px;top:4334px;width:34px;height:34px;background:#4a4a4a}
.divider{left:403px;top:4228px;height:145px;border-left:1px solid #555}
.info{display:flex;align-items:center;gap:16px;color:#9a9a9a}
.info .circle{width:54px;height:54px}
.info small{display:block;font-size:10px;color:#888}
.info strong{font-family:"Roboto Condensed",sans-serif;font-weight:400;font-size:15px;color:#9a9a9a}
.social{top:4313px;width:54px;height:54px;border-radius:50%;background:var(--teal)}
.copy{left:0;top:4426px;width:1200px;text-align:center;font-size:10px;color:#999}
</style>
</head>
<body>
<div class="page">

  <!-- hero -->
  <section class="hero abs"></section>
  <div class="brand abs"><div class="brand-dot"></div><div class="brand-name">MOVA</div></div>
  <nav class="nav abs"><a class="active" href="#">PROFESSIONAL</a><a href="#">JOB COACHING</a><a href="#">BIO</a><a href="#">CONTACT</a></nav>
  <div class="call abs">
    <div class="circle"><svg width="20" height="20" viewBox="0 0 24 24" fill="none" stroke="#fff" stroke-width="2"><path d="M5 3h4l2 5-3 2a11 11 0 0 0 6 6l2-3 5 2v4a2 2 0 0 1-2 2A17 17 0 0 1 3 5a2 2 0 0 1 2-2z"/></svg></div>
    <div><small>Call Now</small><strong>0470/318546</strong></div>
  </div>
  <div class="talk-btn abs"><svg width="18" height="16" viewBox="0 0 24 22" fill="none" stroke="#fff" stroke-width="2"><path d="M3 3h18v12H9l-5 4v-4H3z"/></svg>LET'S TALK</div>

  <div class="portrait abs" role="img" aria-label="Portretfoto van de coach in een rood hemd"></div>
  <div class="years abs"><b>15 YEARS</b><small>of Experience</small></div>

  <h1 class="hero-title abs serif">MET LOOPBAANCHEQUES</h1>
  <div class="hero-sub abs">JOBCOACHING<span>|</span>LOOPBAAN BEGELEIDING</div>
  <p class="hero-text abs">Hello, my name is Daan Verhoef. As a passionate career coach, I want to empower you to do your job every day</p>
  <div class="btn btn-fill abs">GET STARTED NOW</div>
  <div class="btn btn-line abs">LET'S TALK</div>

  <svg class="abs" style="left:0;top:600px" width="1200" height="170" viewBox="0 0 1200 170">
    <path d="M0 110 C140 150 260 140 420 120 C620 90 760 20 930 20 C1050 20 1130 60 1200 100 L1200 170 L0 170 Z" fill="#fff"/>
    <path d="M80 120 C220 145 320 132 440 116 C640 86 780 24 950 26 C1060 28 1140 60 1200 96" fill="none" stroke="var(--teal)" stroke-width="7"/>
  </svg>
  <div class="scroll-line abs"></div>
  <div class="scroll-knob abs"><svg width="22" height="24" viewBox="0 0 22 24" fill="none" stroke="var(--teal)" stroke-width="2"><path d="M2 2l9 20 9-20-9 8z"/></svg></div>
  <div class="scroll-label abs">scroll down</div>

  <!-- help grid -->
  <h2 class="sec-title abs serif" style="top:772px">We Can Help Transform You</h2>
  <p class="sec-sub abs" style="top:820px">What is a better journey? We've identified 6 key elements<br>critical to be a better your experience</p>
  <div class="grid abs">
    <div class="cell"><svg width="64" height="64" viewBox="0 0 64 64" fill="none" stroke="#444" stroke-width="2"><circle cx="32" cy="32" r="26"/><path d="M35 14l-10 20h10l-6 16"/></svg>Hoe kan ik meer energie<br>halen uit mijn job?</div>
    <div class="cell on"><svg width="64" height="64" viewBox="0 0 64 64" fill="none" stroke="#fff" stroke-width="2"><path d="M12 50h40M32 50V12M14 20h36"/><rect x="8" y="22" width="16" height="10"/><path d="M42 22c4-6 12 0 4 8-8-8 0-14-4-8z"/></svg>Hoe vind ik een beter<br>evenwicht tussen werk en privé?</div>
    <div class="cell"><svg width="64" height="64" viewBox="0 0 64 64" fill="none" stroke="#444" stroke-width="2"><circle cx="32" cy="34" r="8"/><path d="M18 58c0-8 6-12 14-12s14 4 14 12M22 14l4 4M42 14l-4 4M32 6v6"/></svg>Wat zijn mijn<br>talenten?</div>
    <div class="cell"><svg width="64" height="64" viewBox="0 0 64 64" fill="none" stroke="#444" stroke-width="2"><circle cx="18" cy="28" r="5"/><circle cx="32" cy="22" r="5"/><circle cx="46" cy="28" r="5"/><path d="M10 52V40h16v12M24 52V32h16v20M38 52V40h16v12"/></svg>Hoe kan ik beter samenwerken<br>met mijn leidinggevende en/of collega's?</div>
    <div class="cell"><svg width="64" height="64" viewBox="0 0 64 64" fill="none" stroke="#444" stroke-width="2"><path d="M20 28h24v14c0 8-6 14-12 14s-12-6-12-14zM24 28v-6M30 28v-8M36 28v-8M42 28v-6M32 6v6M18 10l3 5M46 10l-3 5"/></svg>Misschien vind je dat je meer in<br>je mars hebt dan je vandaag kan tonen?</div>
    <div class="cell"><svg width="64" height="64" viewBox="0 0 64 64" fill="none" stroke="#444" stroke-width="2"><path d="M14 54l14-14M26 26l12 12M30 14l20 20-8 4-16-16zM48 10v8M44 14h8"/></svg>Of weet je wat je wil bereiken,<br>maar durf je destap niet te zetten?</div>
  </div>
  <div class="cta abs">LET'S TALK WITH DAAN VERHOEF <svg width="16" height="10" viewBox="0 0 16 10" fill="none" stroke="#fff" stroke-width="1.5"><path d="M0 5h15M11 1l4 4-4 4"/></svg></div>

  <!-- services -->
  <section class="services abs">
    <h2 class="sec-title abs serif" style="top:48px;color:#fff">Coach, Trainer, Psycholoog</h2>
    <p class="sec-sub abs" style="top:94px;font-size:11px;line-height:21px">de ultieme planningsoplossing voor die hun persoonlijke<br>doelen willen bereiken</p>
    <div class="card abs" style="left:144px"><div class="ph" role="img" aria-label="Foto van een trainer die een groep toespreekt"></div><div class="badge"><svg width="30" height="30" viewBox="0 0 30 30" fill="none" stroke="var(--teal)" stroke-width="1.6"><circle cx="15" cy="9" r="5"/><path d="M5 27c0-6 4-10 10-10s10 4 10 10"/></svg></div><p>Bedrijfscoaching</p></div>
    <div class="card abs" style="left:377px"><div class="ph" role="img" aria-label="Foto van een lachende jonge vrouw" style="background:linear-gradient(180deg,#3a3a3a,#d08a3a)"></div><div class="badge"><svg width="30" height="30" viewBox="0 0 30 30" fill="none" stroke="var(--teal)" stroke-width="1.6"><path d="M4 26L24 6M18 6h6v6"/></svg></div><p>zelfontwikkeling</p></div>
    <div class="card abs" style="left:616px"><div class="ph" role="img" aria-label="Foto van een vergadering in een kantoor" style="background:linear-gradient(180deg,#eef2f4,#8a97a4)"></div><div class="badge"><svg width="30" height="30" viewBox="0 0 30 30" fill="none" stroke="var(--teal)" stroke-width="1.6"><circle cx="8" cy="12" r="3"/><circle cx="15" cy="10" r="3"/><circle cx="22" cy="12" r="3"/><path d="M3 24c0-5 24-5 24 0"/></svg></div><p>Opleiding van net personeel</p></div>
    <div class="card abs" style="left:852px"><div class="ph" role="img" aria-label="Foto van twee mensen in overleg aan tafel" style="background:linear-gradient(180deg,#b8c4cc,#2f3438)"></div><div class="badge"><svg width="30" height="30" viewBox="0 0 30 30" fill="none" stroke="var(--teal)" stroke-width="1.6"><circle cx="15" cy="9" r="4"/><path d="M6 27v-8h18v8M4 19h22"/></svg></div><p>Overleg Plegen</p></div>
    <div class="next abs"><svg width="8" height="10" viewBox="0 0 8 10" fill="none" stroke="#333" stroke-width="1.5"><path d="M2 1l4 4-4 4"/></svg></div>
  </section>

  <!-- explore -->
  <section class="explore abs" role="img" aria-label="Foto van een houten figuur die houten treden opstapt, met een hand die een trede vasthoudt">
    <h2 class="sec-title abs serif" style="top:116px;color:#fff">Explore How can I help you</h2>
    <p class="sec-sub abs" style="top:164px;color:#fff">I am convinced that people are often capable of more than they believe<br>themselves to be. Everything starts with the desire for change.</p>
    <svg class="abs" style="left:0;top:0" width="1200" height="748" viewBox="0 0 1200 748">
      <path d="M284 400 C400 400 500 390 608 336 C700 300 800 290 852 234 C900 200 940 190 960 170" fill="none" stroke="#fff" stroke-width="1.5" stroke-dasharray="5 5"/>
      <circle cx="357" cy="394" r="6" fill="#fff"/><circle cx="608" cy="336" r="6" fill="#fff"/><circle cx="852" cy="234" r="6" fill="#fff"/>
      <path d="M950 160l38-14-14 36-6-14z" fill="none" stroke="#fff" stroke-width="2"/>
    </svg>
    <div class="step abs" style="left:312px;top:522px">Who am I ?</div>
    <div class="step abs" style="left:551px;top:446px">What is my role ?</div>
    <div class="step abs" style="left:778px;top:370px">What do I really want?</div>
  </section>

  <!-- coach -->
  <h2 class="coach-title abs serif">As a job coach</h2>
  <div class="point abs" style="top:2998px"><b>01.</b><p>I don't go for simple quick-wins or ready-made<br>tips and tricks</p></div>
  <div class="point abs" style="top:3073px"><b>02.</b><p>In a spirit of openness, trust and equality, we search together for the deeper insights and sustainable solutions that work for you.</p></div>
  <div class="point abs" style="top:3166px"><b>03.</b><p>Coaching is an awareness process that leads to finding the answers within yourself.</p></div>
  <div class="sign abs" role="img" aria-label="Handtekening van de coach"></div>
  <div class="coach-ring abs"></div>
  <div class="coach-photo abs" role="img" aria-label="Portretfoto van de coach bij een raam"></div>

  <!-- sign up -->
  <section class="signup abs">
    <h2 class="sec-title abs serif" style="top:62px;color:#fff">Sign up</h2>
    <p class="sec-sub abs" style="top:112px;color:#fff;font-size:14px">Sign up today for a no-obligation introductory<br>consultation and take control of your career (again).</p>
    <div class="field abs" style="left:221px;top:211px;width:370px;height:50px"><label>First Name</label><span>Pieter J. Claes</span></div>
    <div class="field abs" style="left:610px;top:211px;width:371px;height:50px"><label>Last Name</label><span>Janssens</span></div>
    <div class="field abs" style="left:221px;top:294px;width:370px;height:51px"><label>Email Address</label><span>lotte.maes@voorbeeld.be</span></div>
    <div class="field abs" style="left:610px;top:294px;width:371px;height:51px"><label>Subject</label><span>The Benefits of Direct Mail Services</span></div>
    <div class="field abs" style="left:221px;top:378px;width:760px;height:115px"><label>Your Message</label><span>Type your message here...</span></div>
  </section>
  <div class="submit abs">SUBMIT NOW</div>

  <!-- footer -->
  <footer class="footer abs"></footer>
  <svg class="abs" style="left:0;top:4050px" width="1200" height="100" viewBox="0 0 1200 100">
    <path d="M0 30 C200 90 420 80 640 50 C860 20 1040 10 1200 60 L1200 100 L0 100 Z" fill="var(--footer)"/>
  </svg>
  <div class="foot-brand abs"><div class="brand-dot"></div><div class="brand-name">MOVA</div></div>
  <div class="cert abs"></div>
  <div class="cert-2 abs"></div>
  <div class="divider abs"></div>
  <div class="info abs" style="left:451px;top:4220px">
    <div class="circle"><svg width="22" height="22" viewBox="0 0 24 24" fill="none" stroke="#fff" stroke-width="2"><path d="M5 3h4l2 5-3 2a11 11 0 0 0 6 6l2-3 5 2v4a2 2 0 0 1-2 2A17 17 0 0 1 3 5a2 2 0 0 1 2-2z"/></svg></div>
    <div><small>Call Now</small><strong>0470/318546</strong></div>
  </div>
  <div class="info abs" style="left:451px;top:4313px">
    <div class="circle"><svg width="22" height="22" viewBox="0 0 24 24" fill="none" stroke="#fff" stroke-width="2"><rect x="3" y="6" width="18" height="12" rx="1"/><path d="M3 7l9 6 9-6"/></svg></div>
    <div><small>Location</small><strong>12 Lindenlaan, Bureau 4, Gent</strong></div>
  </div>
  <div class="info abs" style="left:811px;top:4220px">
    <div class="circle"><svg width="22" height="22" viewBox="0 0 24 24" fill="none" stroke="#fff" stroke-width="2"><rect x="3" y="6" width="18" height="12" rx="1"/><path d="M3 7l9 6 9-6"/></svg></div>
    <div><small>Email Address</small><strong>daan.verhoef@movacoaching.be</strong></div>
  </div>
  <div class="social abs" style="left:811px"></div>
  <div class="social abs" style="left:880px"></div>
  <div class="social abs" style="left:950px"></div>
  <p class="copy abs">©2023 Mova Coaching. All Rights Reserved.</p>
</div>
</body>
</html>
```